Business Card Design Project

- makeup artist business card

- original and creative

- Elegant design

- Feel free to come out with cool designs but stick to being elegant and attractive

- Design relates to makeup

- includes name, occupation, contact numbers, email, website

- regular size business card

- round corner card

- double sided

- on 1 side it should just have the website name in the center " browsandblush.example "

Industry/Entity Type

Business

Requirements
Must have
• Marla Voss
Makeup Artist
USA: +1 (415)872-6410
Singapore: +65 83027715
marlavoss@browsandblush.example
www.browsandblush.example
Should not have
• nothing cartoon looking.
Pictures of makeup being grab from the internet.. Examples: eyes or lips.

```html
<!DOCTYPE html>
<html lang="en">
<head>
<meta charset="utf-8">
<title>Marla Voss – Makeup Artist Business Card</title>
<link rel="stylesheet" href="https://fonts.googleapis.com/css2?family=Source+Sans+3:wght@400;600;700&display=swap">
<style>
  :root {
    --page: #ffffff;
    --card: #2e0b0c;
    --accent: #a8373b;
    --accent-soft: #b9484b;
    --band: #7d2a2d;
    --edge: #1a0506;
  }
  * { margin: 0; padding: 0; box-sizing: border-box; }
  html, body {
    width: 840px;
    height: 1200px;
    overflow: hidden;
    background: var(--page);
    font-family: "Source Sans 3", "Myriad Pro", Arial, sans-serif;
  }
  .canvas {
    position: relative;
    width: 840px;
    height: 1200px;
  }
  .card {
    position: absolute;
    left: 0;
    width: 840px;
    background: var(--card);
    border-radius: 30px;
    box-shadow: 0 0 0 1px var(--edge);
    overflow: hidden;
  }
  .card--front { top: 0; height: 555px; }
  .card--back { top: 700px; height: 500px; border-bottom-left-radius: 0; border-bottom-right-radius: 0; }

  .wave-band {
    position: absolute;
    left: 0;
    width: 100%;
    background: linear-gradient(180deg, var(--band), #6a2326 50%, var(--band));
    opacity: 0.85;
  }
  .wave-band--top { top: 62px; height: 100px; }
  .wave-band--bottom { top: 405px; height: 108px; }

  .site-name {
    position: absolute;
    left: 0;
    right: 0;
    top: 258px;
    padding-left: 60px;
    text-align: center;
    color: var(--accent);
    font-weight: 700;
    font-size: 45px;
    letter-spacing: 0.2px;
  }

  .identity {
    position: absolute;
    right: 20px;
    top: 40px;
    text-align: left;
  }
  .identity__name {
    color: var(--accent);
    font-weight: 700;
    font-size: 43px;
    line-height: 1;
  }
  .identity__role {
    color: var(--accent-soft);
    font-weight: 400;
    font-size: 29px;
    margin-top: 10px;
  }

  .contact {
    position: absolute;
    left: 36px;
    top: 232px;
    color: var(--accent-soft);
  }
  .contact__title {
    color: var(--accent);
    font-weight: 700;
    font-size: 36px;
    margin-bottom: 18px;
  }
  .contact__list { list-style: none; }
  .contact__item {
    font-size: 28px;
    line-height: 41px;
  }
</style>
</head>
<body>
<main class="canvas">
  <section class="card card--front">
    <div class="wave-band wave-band--top" role="img" aria-label="Band of repeated wavy lines in soft red"></div>
    <p class="site-name">browsandblush.example</p>
    <div class="wave-band wave-band--bottom" role="img" aria-label="Band of repeated wavy lines in soft red"></div>
  </section>

  <section class="card card--back">
    <div class="identity">
      <h1 class="identity__name">Marla Voss</h1>
      <p class="identity__role">Makeup Artist</p>
    </div>
    <div class="contact">
      <h2 class="contact__title">Contact</h2>
      <ul class="contact__list">
        <li class="contact__item">USA: +1 (415)872-6410</li>
        <li class="contact__item">Singapore: +65 83027715</li>
        <li class="contact__item">marlavoss@browsandblush.example</li>
        <li class="contact__item">www.browsandblush.example</li>
      </ul>
    </div>
  </section>
</main>
</body>
</html>
```